Business card design + letter head + PowerPoint template

Please design a business card (front and back) for our e-commerce website specializing in renting out maternity clothing. Logo provided. The logo is green with white letters and I would quite like to have a different color on the back of the business card so that it is a full color rather than just white. An other option would be to use the green from the logo on the back and make the logo white so that it stands out. Company name is CradleNest and, if it looks good, you can use the strap line "Your unlimited online maternity wardrobe" and "Votre dressing maternité illimité" on the reverse side of the business card. On the front side, please use icons for Telephone, Email, street address and website instead of words. Please use a dummy name, e.g. Mark Dowley, for the person's name. All details (name, address, telephone, etc.) will be supplied to the winning designer to complete after the contest. Format: 85mm x 55mm.
Please also design a letter head and a PowerPoint template that I can paste into the background of my presentations. Please use something light (not heavy) that won't take up too much room in my files. I would prefer something minimalist.

```html
<!DOCTYPE html>
<html lang="en">
<head>
<meta charset="utf-8">
<title>CradleNest — Stationery</title>
<link href="https://fonts.googleapis.com/css2?family=Roboto:wght@400;500;700&family=Great+Vibes&display=swap" rel="stylesheet">
<style>
  :root {
    --teal: #3a9a86;
    --teal-faint: #e3efe9;
    --ink: #4a4a4a;
    --ink-soft: #6b6b6b;
    --card: #f4f4f2;
    --paper: #f8f7f3;
    --stage: #e8e5df;
    --white: #ffffff;
  }
  * { box-sizing: border-box; margin: 0; padding: 0; }
  html, body { width: 1200px; height: 913px; overflow: hidden; }
  body {
    background: var(--stage);
    font-family: "Roboto", Arial, sans-serif;
    color: var(--ink);
    position: relative;
  }

  /* Business cards */
  .card {
    position: absolute;
    left: 73px;
    width: 378px;
    box-shadow: 0 2px 6px rgba(0,0,0,.18);
  }
  .card--front { background: var(--card); height: 216px; }
  .card--front-a { top: 107px; }
  .card--front-b { top: 351px; height: 225px; }
  .card--back { top: 607px; height: 213px; background: var(--teal); color: var(--white); }

  .card__person { position: absolute; left: 56px; top: 52px; }
  .card__name { font-size: 17px; font-weight: 700; color: var(--teal); line-height: 1.1; }
  .card--front-b .card__name { color: var(--ink); }
  .card__role { font-size: 11px; color: var(--ink); margin-top: 2px; }
  .card__address { position: absolute; left: 56px; top: 100px; font-size: 9px; line-height: 13px; color: var(--ink-soft); }
  .card__contacts { position: absolute; left: 56px; top: 138px; list-style: none; font-size: 9px; line-height: 12.5px; color: var(--ink-soft); }
  .card__contacts li { display: flex; align-items: center; gap: 5px; }
  .card__contacts svg { width: 7px; height: 7px; fill: var(--teal); flex: none; }

  .wordmark {
    position: absolute;
    display: flex;
    align-items: center;
    gap: 6px;
    font-family: "Roboto", Arial, sans-serif;
    font-weight: 500;
    color: var(--teal);
  }
  .wordmark__dot { border-radius: 50%; background: var(--teal); flex: none; }
  .card--front .wordmark { left: 208px; top: 90px; font-size: 22px; }
  .card--front .wordmark__dot { width: 16px; height: 16px; }
  .card--back .wordmark { left: 128px; top: 58px; font-size: 26px; color: var(--white); }
  .card--back .wordmark__dot { width: 18px; height: 18px; background: var(--white); }

  .card__tagline { position: absolute; left: 0; right: 0; top: 166px; text-align: center; font-size: 11px; line-height: 14px; }

  /* Letterhead */
  .letterhead {
    position: absolute;
    left: 500px; top: 76px;
    width: 600px; height: 775px;
    background: var(--paper);
    box-shadow: 0 2px 8px rgba(0,0,0,.18);
    overflow: hidden;
  }
  .letterhead__backdrop { position: absolute; left: 0; top: 0; width: 600px; height: 775px; }
  .letterhead .wordmark--head { left: 44px; top: 40px; font-size: 24px; }
  .wordmark--head .wordmark__dot { width: 18px; height: 18px; }
  .letterhead__contact { position: absolute; left: 429px; top: 29px; font-size: 9px; line-height: 12.5px; color: var(--ink-soft); }
  .letterhead__contact ul { list-style: none; }
  .letterhead__contact li { display: flex; align-items: center; gap: 5px; }
  .letterhead__contact svg { width: 7px; height: 7px; fill: var(--teal); }

  .letter { position: absolute; left: 44px; top: 175px; width: 512px; font-size: 8.8px; line-height: 14.6px; color: var(--ink-soft); }
  .letter__meta { line-height: 13px; }
  .letter__subject { margin-top: 12px; }
  .letter__greeting { margin-top: 28px; }
  .letter p.letter__para { margin-top: 13px; }
  .letter__closing { margin-top: 36px; font-size: 10px; }
  .letter__signature { font-family: "Great Vibes", cursive; font-size: 19px; color: var(--ink); margin-top: 6px; }
</style>
</head>
<body>

<svg width="0" height="0" style="position:absolute">
  <defs>
    <symbol id="icon-phone" viewBox="0 0 10 10"><path d="M2.2 0.5 3.8 2.6 2.9 3.7C3.5 5 4.9 6.5 6.3 7.1L7.4 6.2 9.5 7.8 8.6 9.5C4.6 9.3 0.7 5.4 0.5 1.4Z"/></symbol>
    <symbol id="icon-mail" viewBox="0 0 10 10"><path d="M0.5 2H9.5V8H0.5ZM1.2 2.6 5 5.4 8.8 2.6Z"/></symbol>
    <symbol id="icon-globe" viewBox="0 0 10 10"><circle cx="5" cy="5" r="4.5"/></symbol>
  </defs>
</svg>

<!-- Front card, teal name -->
<section class="card card--front card--front-a">
  <div class="card__person">
    <p class="card__name">Mark Dowley</p>
    <p class="card__role">Managing Director</p>
  </div>
  <p class="card__address">1187 Harbor Ridge Ave.<br>Tampa, FL 33611</p>
  <ul class="card__contacts">
    <li><svg><use href="#icon-phone"/></svg>(555) 204-3187</li>
    <li><svg><use href="#icon-mail"/></svg>info@cradlenest.com</li>
    <li><svg><use href="#icon-globe"/></svg>www.cradlenest.com</li>
  </ul>
  <div class="wordmark"><span class="wordmark__dot"></span>cradlenest</div>
</section>

<!-- Front card, dark name -->
<section class="card card--front card--front-b">
  <div class="card__person">
    <p class="card__name">Mark Dowley</p>
    <p class="card__role">Managing Director</p>
  </div>
  <p class="card__address">1187 Harbor Ridge Ave.<br>Tampa, FL 33611</p>
  <ul class="card__contacts">
    <li><svg><use href="#icon-phone"/></svg>(555) 204-3187</li>
    <li><svg><use href="#icon-mail"/></svg>info@cradlenest.com</li>
    <li><svg><use href="#icon-globe"/></svg>www.cradlenest.com</li>
  </ul>
  <div class="wordmark"><span class="wordmark__dot"></span>cradlenest</div>
</section>

<!-- Back card -->
<section class="card card--back">
  <div class="wordmark"><span class="wordmark__dot"></span>cradlenest</div>
  <p class="card__tagline">Your unlimited online maternity wardrobe<br>Votre dressing maternité illimité</p>
</section>

<!-- Letterhead -->
<article class="letterhead">
  <svg class="letterhead__backdrop" viewBox="0 0 600 775" aria-hidden="true">
    <circle cx="395" cy="480" r="170" fill="var(--teal-faint)" opacity=".55"/>
    <text x="225" y="498" font-family="Roboto, Arial, sans-serif" font-weight="500" font-size="92" fill="#ffffff" opacity=".75">cradlenest</text>
  </svg>

  <div class="wordmark wordmark--head"><span class="wordmark__dot"></span>cradlenest</div>

  <address class="letterhead__contact" style="font-style:normal">
    <p>1187 Harbor Ridge Ave.</p>
    <p>Tampa, FL 33611</p>
    <ul>
      <li><svg><use href="#icon-phone"/></svg>(555) 204-3187</li>
      <li><svg><use href="#icon-mail"/></svg>info@cradlenest.com</li>
      <li><svg><use href="#icon-globe"/></svg>www.cradlenest.com</li>
    </ul>
  </address>

  <div class="letter">
    <div class="letter__meta">
      <p>Date : 25 July 2017</p>
      <p>Brightpath Legal</p>
      <p>48 Meadow Lane</p>
    </div>
    <p class="letter__subject">Sub: How to change our business Policy</p>
    <p class="letter__greeting">Dear Hayes,</p>
    <p class="letter__para">Brightpath Legal is an entrepreneurial law firm that provides value-driven services to businesses at every stage of their life cycle. We believe that to effectively counsel a growing business, a lawyer must do more than provide legal advice. We know you need insights and tactics you can use and apply in the real world. A true "startup lawyer" must act as both a shield and a sword: protecting you, but — more importantly — helping you decide which risks are worth taking to grow.</p>
    <p class="letter__para">We pride ourselves on going above and beyond the role of traditional attorneys. We take the time to understand your business goals. We're firm believers that effective legal advice does not exist — and can't be given — in a vacuum.</p>
    <p class="letter__para">We value our clients and strive to be more than just a hired gun. We want to be part of your team. We're looking for true partners. We're looking to grow together. We know you don't like surprises (neither do we!) so we're upfront about project costs and timelines. When we give you a proposed budget or timeline, it's not a guess. We're making a promise that we intend to keep. By leveraging our unique combination of big law firm, in-house counsel and startup experience, we provide real-time, pragmatic and actionable advice.</p>
    <p class="letter__para">So whether you're an entrepreneur with an idea, a new startup, an emerging company looking to grow, or an established business on the verge of taking things to the next level, we want to work with you.</p>
    <p class="letter__closing">Warm Regards</p>
    <p class="letter__signature">Elena Ward</p>
  </div>
</article>

</body>
</html>
```